Webdesign für Beratung von Firmen zum Thema Radon
Zielgruppe
Firmenname: Lumivelde - Ich informiere und berate als Radon Fachperson, Privatpersonen sowie Firmen zum Thema Radon, und die Gefahren die damit verbunden sind in bestehenden Gebäuden und Neubauten. Die Leistung erfolgt in Form eines ausgearbeiteten Sanierungskonzeptes bzw. bautechnische Maßnahmen beim Neubau.
Aufgabenstellung
Keep it simple and clean, weniger ist mehr. Die beigefügten Info-Grafiken sollen nur als Information dienen zum Thema Radon, und sollen nicht verwendet werden - ich hoffe hier doch besseres Bildmaterial von euch zu bekommen :-)

```html
<!DOCTYPE html>
<html lang="de">
<head>
<meta charset="utf-8">
<title>Lumivelde – Radon Beratung</title>
<link rel="stylesheet" href="https://fonts.googleapis.com/css2?family=Outfit:wght@300;400;500;600;700;800&display=swap">
<style>
:root{
  --yellow:#f6b443;
  --yellow-dark:#e9a22c;
  --ink:#3c3c3e;
  --text:#505054;
  --muted:#8a8a8e;
  --line:#e4e4e6;
  --mauve:#7b6f80;
  --panel:#f2f2f3;
  --white:#ffffff;
}
*{box-sizing:border-box;margin:0;padding:0}
html,body{width:1200px;height:2996px;overflow:hidden}
body{position:relative;background:var(--white);font-family:"Outfit",sans-serif;color:var(--text);font-size:12px;line-height:1.55}
.abs{position:absolute}
.hero-photo{left:0;top:0;width:1200px;height:760px;background:linear-gradient(180deg,#d9dee0 0%,#b9c6bf 14%,#4f6b43 30%,#6d8a4f 44%,#8aa05f 47%,#6e8468 55%,#a9b5b0 70%,#e8ecec 86%,#ffffff 100%)}
.site-header .logo{left:244px;top:26px;display:flex;align-items:center;gap:8px;color:var(--ink);font-weight:700;font-size:14px;letter-spacing:.5px}
.logo-mark{width:14px;height:14px;border-radius:50%;background:var(--yellow)}
.nav{left:421px;top:26px;display:flex;gap:0;font-size:11px;color:var(--ink)}
.nav a{color:inherit;text-decoration:none;position:absolute;white-space:nowrap}
.phone{left:858px;top:27px;font-size:11px;color:var(--ink);display:flex;gap:8px}
.phone small{display:block;text-decoration:underline;color:var(--muted);font-size:10px;line-height:1.2}
.hero-title{left:233px;top:152px;font-size:92px;font-weight:800;color:var(--white);letter-spacing:2px;line-height:1}
.hero-lead{left:234px;top:255px;width:355px;color:var(--white);font-size:11px;line-height:1.45}
.btn{display:flex;align-items:center;justify-content:center;border-radius:8px;font-size:11px;color:var(--ink);background:linear-gradient(180deg,#fcc55e,var(--yellow));box-shadow:0 4px 0 var(--yellow-dark),0 8px 16px rgba(246,180,67,.35)}
.hero-btn{left:421px;top:312px;width:145px;height:30px}
.hotspot-label{color:var(--white);font-size:10.5px}
.portrait{left:233px;top:442px;width:258px;height:330px;border-radius:0 0 40px 0;background:linear-gradient(180deg,rgba(150,150,150,0) 0%,#9aa3a8 45%,#8e979d 100%)}
.badge{left:238px;top:715px;width:76px;height:76px;border-radius:50%;background:var(--yellow)}
.badge-text{left:259px;top:740px;font-size:11.5px;color:var(--ink);line-height:1.2}
.badge-text b{font-weight:600;display:block}
.about-title{left:416px;top:596px;font-size:62px;font-weight:600;color:var(--ink);line-height:1}
.about-copy{left:538px;top:680px;width:400px;font-size:10.5px}
.about-copy p{margin-bottom:9px}
.about-note{left:314px;top:775px;font-size:10.5px;line-height:1.45}
.rule{background:var(--line)}
.arrows{left:314px;top:828px;width:70px;height:22px;border:1px solid var(--line);border-radius:11px;display:flex}
.arrows span{flex:1;display:flex;align-items:center;justify-content:center;color:var(--yellow);font-size:13px}
.contact-frame{left:538px;top:811px;width:166px;height:54px;border:1px solid var(--line);border-radius:6px;background:var(--white)}
.btn-mauve{left:550px;top:822px;width:145px;height:32px;border-radius:7px;background:var(--mauve);color:var(--white);font-size:11px;display:flex;align-items:center;justify-content:center;box-shadow:0 4px 0 #5e5363}
.side-tag{font-size:9.5px;color:var(--muted);line-height:1.25;border-left:2px solid var(--yellow);padding-left:6px}
.ghost{color:#f3f3f4;font-weight:800;line-height:1}
.section-title{font-size:58px;font-weight:600;color:var(--ink);line-height:1}
.section-title em{font-style:normal;color:var(--yellow)}
.info-item{left:247px;width:360px}
.info-item h3{font-size:15px;font-weight:500;color:var(--ink);border-left:3px solid var(--yellow);padding-left:14px;margin-left:-3px;line-height:1.2;margin-bottom:14px}
.info-item p,.info-item ol{font-size:10.5px;padding-left:15px}
.info-item ol{list-style:none}
.house-form{left:735px;top:1140px;width:240px;color:var(--white)}
.house-form h4{font-size:15px;font-weight:600;line-height:1.25}
.house-form p{font-size:10.5px;line-height:1.35;margin-top:4px}
.field-dark{left:733px;width:171px;height:31px;border:1px solid rgba(255,255,255,.75);border-radius:6px;color:var(--white);font-size:9.5px;padding:9px 18px}
.form-btn{left:733px;top:1312px;width:172px;height:31px}
.lab-photo{left:0;top:1553px;width:471px;height:494px;background:linear-gradient(135deg,#dfe3e6 0%,#c7ccd0 35%,#e9ebed 60%,#bfc4c7 100%)}
.ways-card{left:277px;top:1442px;width:166px;height:175px;background:var(--white);border-radius:6px;box-shadow:0 10px 30px rgba(0,0,0,.06)}
.ways-card .num{position:absolute;left:0;right:0;top:-12px;text-align:center;font-size:120px;font-weight:800;color:#f0f0f1;line-height:1}
.ways-card p{position:absolute;left:24px;right:18px;bottom:22px;font-size:10.5px;color:var(--ink);line-height:1.45}
.callout{left:626px;top:1498px;width:339px;height:72px;border:1px solid var(--line);border-left:none}
.callout p{position:absolute;left:157px;top:21px;font-size:10.5px;line-height:1.5}
.callout span{color:var(--yellow)}
.service{left:518px;width:450px}
.service h3{font-size:15px;font-weight:500;color:var(--ink);margin-bottom:14px}
.service .lead{font-weight:600;color:var(--ink);font-size:10.5px;margin-bottom:20px;line-height:1.5}
.service p.body{font-size:10.5px;line-height:1.5}
.service ul{list-style:none;font-size:10.5px;line-height:1.5;margin-left:4px}
.service li{padding-left:12px;position:relative}
.service li::before{content:"";position:absolute;left:0;top:7px;width:4px;height:4px;border-radius:50%;background:var(--yellow)}
.ref-intro{left:566px;top:2169px;font-size:10.5px;line-height:1.5}
.ref-card{top:2241px}
.ref-card .img{height:143px}
.ref-card h3{font-size:15px;font-weight:500;color:var(--ink);margin:15px 0 10px}
.ref-card p{font-size:10.5px;line-height:1.5}
.contact-band{left:0;top:2580px;width:1200px;height:416px;background:var(--panel)}
.warte{left:235px;top:2553px;width:356px;height:90px;background:var(--white);border-radius:6px;box-shadow:0 12px 24px rgba(0,0,0,.08);font-size:47px;font-weight:700;color:var(--ink);display:flex;align-items:center;justify-content:center;letter-spacing:.5px}
.schreiben{left:237px;top:2656px;font-size:66px;font-weight:800;color:var(--yellow);line-height:1;letter-spacing:1px}
.gleich{left:237px;top:2728px;font-size:54px;font-weight:400;color:var(--ink);line-height:1}
.pointer{left:628px;top:2580px;width:0;height:0;border-left:14px solid transparent;border-right:14px solid transparent;border-top:14px solid var(--white)}
.contact-lead{left:614px;top:2620px;width:356px;font-size:10.5px;line-height:1.5}
.field{width:170px;height:36px;border:1px solid #c9c9cc;border-radius:6px;font-size:10.5px;color:var(--muted);padding:10px 12px;background:transparent}
.consent{left:585px;top:2871px;width:198px;font-size:8.5px;text-align:right;line-height:1.3;color:var(--muted)}
.submit{left:794px;top:2868px;width:171px;height:31px}
.footer-rule{left:235px;top:2936px;width:730px;height:1px;background:#dcdcdf}
.footer{top:2960px;font-size:9.5px;color:var(--muted)}
</style>
</head>
<body>

<div class="abs hero-photo" role="img" aria-label="Foto: Holzhaus am Bergsee mit Nadelwald im Nebel, im Wasser gespiegelt"></div>

<header class="site-header">
  <div class="abs logo"><span class="logo-mark"></span>LUMIVELDE</div>
  <nav class="abs nav">
    <a style="left:0">Über uns</a>
    <a style="left:77px">Was ist radon</a>
    <a style="left:156px">Leistung</a>
    <a style="left:226px">Referenzen</a>
    <a style="left:302px">Kontakt</a>
  </nav>
  <div class="abs phone">
    <svg width="12" height="12" viewBox="0 0 24 24" style="margin-top:2px"><path d="M6.6 10.8a15 15 0 0 0 6.6 6.6l2.2-2.2c.3-.3.7-.4 1-.2 1.1.4 2.3.6 3.6.6.6 0 1 .4 1 1V20c0 .6-.4 1-1 1A17 17 0 0 1 3 4c0-.6.4-1 1-1h3.5c.6 0 1 .4 1 1 0 1.3.2 2.5.6 3.6.1.3 0 .7-.2 1z" fill="none" stroke="#f6b443" stroke-width="2"/></svg>
    <div>8 (800) <b>314 - 7090</b><small>Einen Anruf bestellen</small></div>
  </div>
</header>

<h1 class="abs hero-title">LUMIVELDE</h1>
<p class="abs hero-lead"><b>Wir informieren und beraten</b> Privatpersonen sowie Firmen zum Thema Radon, und die Gefahren die damit verbunden sind in bestehenden Gebäuden und Neubauten.</p>
<a class="abs btn hero-btn">Bewerbung abgeben</a>

<svg class="abs" style="left:0;top:0" width="1200" height="620" aria-hidden="true">
  <g stroke="#fff" stroke-width="1" fill="none">
    <line x1="642" y1="366" x2="642" y2="460"/>
    <line x1="713" y1="320" x2="713" y2="565"/>
    <line x1="759" y1="351" x2="759" y2="484"/>
    <line x1="812" y1="323" x2="812" y2="455"/>
    <circle cx="642" cy="360" r="6"/><circle cx="713" cy="314" r="6"/>
    <circle cx="759" cy="345" r="6"/><circle cx="812" cy="317" r="6"/>
  </g>
  <g fill="#fff"><circle cx="642" cy="360" r="2"/><circle cx="713" cy="314" r="2"/><circle cx="759" cy="345" r="2"/><circle cx="812" cy="317" r="2"/></g>
</svg>
<span class="abs hotspot-label" style="left:653px;top:445px">Abfluss</span>
<span class="abs hotspot-label" style="left:769px;top:468px">Risse im Boden</span>
<span class="abs hotspot-label" style="left:820px;top:442px">Grundwasser</span>
<span class="abs hotspot-label" style="left:722px;top:551px">Bodenablauf</span>

<!-- Über uns -->
<div class="abs portrait" role="img" aria-label="Foto: Berater mit Brille und grauem T-Shirt, Arme verschränkt"></div>
<div class="abs badge"></div>
<div class="abs badge-text"><b>Jonas FERBER</b>Beratung</div>
<h2 class="abs about-title">Über UNS</h2>
<div class="abs about-copy">
  <p>Lorem ipsum dolor sit amet, consectetur adipiscing elit, sed do eiusmod tempor incididunt ut labore et dolore magna aliqua. Quis ipsum suspendisse ultrices gravida. Risus commodo viverra maecenas accumsan lacus vel facilisis.</p>
  <p>Lorem ipsum dolor sit amet, consectetur adipiscing elit, sed do eiusmod tempor incididunt ut labore et dolore magna aliqua. Quis ipsum suspendisse ultrices gravida. Risus commodo viverra maecenas accumsan lacus vel facilisis.</p>
</div>
<p class="abs about-note">Für weitere Informationen<br>kontaktieren Sie uns bitte</p>
<div class="abs rule" style="left:233px;top:838px;width:732px;height:1px"></div>
<div class="abs arrows" style="background:#fff"><span style="color:#ccc">←</span><span style="border-left:1px solid var(--line)">→</span></div>
<div class="abs contact-frame"></div>
<a class="abs btn-mauve">Kontaktieren sie unsa</a>
<svg class="abs" style="left:806px;top:806px" width="18" height="28" aria-hidden="true"><rect x="1.5" y="1.5" width="15" height="21" rx="7.5" fill="#fff" stroke="#f6b443" stroke-width="1.5"/><line x1="9" y1="6" x2="9" y2="10" stroke="#f6b443" stroke-width="1.5"/><line x1="9" y1="23" x2="9" y2="28" stroke="#f6b443"/></svg>
<div class="abs side-tag" style="left:815px;top:888px">Ein paa r Worte<br>über Radon</div>

<!-- Was ist Radon -->
<div class="abs ghost" style="left:-20px;top:960px;font-size:170px">03</div>
<div class="abs ghost" style="left:215px;top:965px;font-size:66px;transform:rotate(-90deg);transform-origin:0 0;translate:-52px 525px;letter-spacing:2px">INFORMATION</div>
<div class="abs ghost" style="left:596px;top:1035px;font-size:170px;color:#f4f4f5">3,8</div>
<h2 class="abs section-title" style="left:235px;top:968px"><em>Was</em> ist RADON</h2>

<div class="abs info-item" style="top:1064px"><h3>Die isotope des Radons</h3><p>Radon ist ein naturlich vorkommendes radioaktives Gas,<br>das man nicht sehen, riechen oder schmecken kann.</p></div>
<div class="abs info-item" style="top:1163px;width:380px"><h3>Warum ist es gefahrlich?</h3><ol><li>1. Radon ist die zweithaufigste Ursache fur Lungenkrebs</li><li>2. Radon haftet an staub oder Tabakrauch und gelangt in die Lunge.</li><li>3. Die meiste Exposition tritt in Haushalten auf</li></ol></div>
<div class="abs info-item" style="top:1270px"><h3>Radon und Passivrauchen</h3><p>Das einatmen von Radon ist gefahrlich, aber es ist noch<br>schadlicher, wenn Sie auch Tabakrauch einatmen.</p></div>

<div class="abs rule" style="left:235px;top:1375px;width:350px;height:1px"></div>
<div class="abs" style="left:573px;top:1338px;font-size:40px;font-weight:700;color:#d8d8da;line-height:1">?</div>
<div class="abs" style="left:581px;top:1370px;width:6px;height:6px;border-radius:50%;background:var(--yellow)"></div>
<span class="abs" style="left:594px;top:1368px;font-size:9.5px;color:var(--muted)">Was tun</span>
<div class="abs rule" style="left:583px;top:1382px;width:1px;height:56px"></div>
<svg class="abs" style="left:575px;top:1437px" width="18" height="24" aria-hidden="true"><rect x="1.5" y="1.5" width="15" height="21" rx="7.5" fill="#fff" stroke="#f6b443" stroke-width="1.5"/><line x1="9" y1="6" x2="9" y2="10" stroke="#f6b443" stroke-width="1.5"/></svg>

<svg class="abs" style="left:655px;top:950px" width="545" height="545" role="img" aria-label="Foto: weißes Holzhaus mit spitzem Dach vor Hügeln und Wiese">
  <defs><linearGradient id="houseTones" x1="0" y1="0" x2="0" y2="1"><stop offset="0" stop-color="#c9c7c3"/><stop offset=".45" stop-color="#8d8a84"/><stop offset=".75" stop-color="#6e7a4c"/><stop offset="1" stop-color="#9aa265"/></linearGradient></defs>
  <path d="M545 10 C470 40 420 110 350 140 L170 0 C120 80 90 120 60 150 C10 170 0 240 5 300 C15 360 80 380 160 390 C280 400 420 420 545 545 Z" fill="url(#houseTones)"/>
</svg>
<div class="abs house-form"><h4>Die Radonhalbwertszeit<br>beträgt nur 3,8 Tage</h4><p>Die Entfernung oder Isolierung der Quelle reduziert die Bedrohung erheblich.</p></div>
<div class="abs field-dark" style="top:1223px">Name</div>
<div class="abs field-dark" style="top:1264px">Telefonnummer</div>
<a class="abs btn form-btn">Absenden</a>

<!-- Leistung -->
<div class="abs lab-photo" role="img" aria-label="Foto: Laborantin im weißen Kittel an einem Labortisch mit Glasflaschen"></div>
<div class="abs ways-card"><div class="num">3</div><p><b>Es gibt 3 Hauptwege</b>, um die Radonkonzentration in Häusern zu reduzieren:</p></div>
<div class="abs callout"><p><span>Kontaktieren Sie</span> uns und wir<br>können Ihnen mit Radon helfen</p></div>
<h2 class="abs section-title" style="left:512px;top:1524px"><em>Leis</em>tung</h2>
<div class="abs ghost" style="left:470px;top:1625px;font-size:130px;color:#eeeeef">01</div>
<div class="abs ghost" style="left:470px;top:1885px;font-size:130px;color:#eeeeef">02</div>

<div class="abs service" style="top:1642px">
  <h3>Begutachtung und Beratung</h3>
  <p class="lead">Bei der Berücksichtigung des Isotopengehalts von Radon sollte auch die Aktivität der nichtflüchtigen Zerfallsprodukte (Isotope von Polonium, Blei, Wismut usw.) mit unterschiedlichen Halbwertszeiten berücksichtigt werden.</p>
  <p class="body">Für die Analyse wurden entsprechende Anleitungen entwickelt. Das Kit zur Messung des Radongehalts enthält einen Kollektor, der im Erdgeschoss eines Wohngebäudes für einen Zeitraum von 2-7 Tagen installiert werden muss. Als nächstes wird der Kollektor zur Analyse ins Labor geschickt. Instrumente zur Langzeitmessung (bis zu einem Jahr) des Radongehalts sind ebenfalls erhältlich. Es ist möglich, die aus dem Boden freigesetzte Radonmenge vor Baubeginn zu messen. Die Radonkonzentration kann sich täglich ändern, daher sind Langzeitmessungen der durchschnittlichen Radonkonzentration in Räumen erforderlich, in denen sich eine Person viel Zeit aufhält.</p>
</div>
<div class="abs service" style="top:1901px">
  <h3>Begutachtung und Beratung</h3>
  <p class="lead">Es gibt 3 Hauptwege, um die Radonkonzentration in Häusern zu reduzieren:</p>
  <ul><li>Verbesserung der Belüftung des Raumes und Verhinderung des Eindringens<br>von Radon aus dem Keller in die Wohnräume</li><li>Installation eines Systems zur Entfernung von Radon aus Kellern</li><li>Installation von Überdruckbelüftungssystemen</li></ul>
</div>

<div class="abs rule" style="left:399px;top:2047px;width:1px;height:84px"></div>
<div class="abs side-tag" style="left:401px;top:2121px">Unser Ergebnis</div>

<!-- Referenzen -->
<h2 class="abs section-title" style="left:235px;top:2145px"><em>Referen</em>zen</h2>
<p class="abs ref-intro">Sehen Sie sich das Ergebnis<br>unserer Arbeit an</p>

<article class="abs ref-card" style="left:235px;width:203px"><div class="img" role="img" aria-label="Foto: zwei runde Lüftungsöffnungen in heller Betonwand" style="background:linear-gradient(135deg,#e4e3df,#c9c8c3)"></div><h3>Kanal Umbau</h3><p>Lorem ipsum dolor sit amet, consectetur adipiscing elit, sed do eiusmod tempor incididunt ut labore et dolore magna aliqua. Quis ipsum suspendisse ultrices gravida. Risus commodo viverra maecenas</p></article>
<article class="abs ref-card" style="left:483px;width:215px"><div class="img" role="img" aria-label="Foto: zwei runde Lüftungsgitter in Ziegelwand" style="background:linear-gradient(135deg,#8a5a44,#6f4a3a 50%,#8b9c96)"></div><h3>Strömungserweiterung</h3><p>Lorem ipsum dolor sit amet, consectetur adipiscing elit, sed do eiusmod tempor incididunt ut labore et dolore magna aliqua. Quis ipsum suspendisse ultrices gravida. Risus commodo viverra maecenas</p></article>
<article class="abs ref-card" style="left:749px;width:216px"><div class="img" role="img" aria-label="Foto: runder Lüftungsauslass an weißer Decke" style="background:linear-gradient(135deg,#eef1f6,#c9d1dc)"></div><h3>Lüftungsanlage</h3><p>Lorem ipsum dolor sit amet, consectetur adipiscing elit, sed do eiusmod tempor incididunt ut labore et dolore magna aliqua. Quis ipsum suspendisse ultrices gravida. Risus commodo viverra maecenas</p></article>

<!-- Kontakt -->
<div class="abs contact-band"></div>
<div class="abs pointer"></div>
<svg class="abs" style="left:630px;top:2550px" width="18" height="24" aria-hidden="true"><rect x="1.5" y="1.5" width="15" height="21" rx="7.5" fill="none" stroke="#f6b443" stroke-width="1.5"/><line x1="9" y1="6" x2="9" y2="10" stroke="#f6b443" stroke-width="1.5"/></svg>
<p class="abs" style="left:656px;top:2550px;font-size:9px;line-height:1.2;color:var(--muted)">Lösen Sie mit uns Ihr<br>Radonproblem</p>
<div class="abs warte">WARTE NICHT!</div>
<div class="abs schreiben">SCHREIBEN</div>
<div class="abs gleich">Sie uns gleich!</div>
<p class="abs contact-lead">Sed ut perspiciatis unde omnis iste natus error sit voluptatem accusantium doloremque laudantium, totam rem aperiam, eaque ipsa.</p>
<div class="abs field" style="left:614px;top:2673px">Name</div>
<div class="abs field" style="left:795px;top:2673px">Varname</div>
<div class="abs field" style="left:614px;top:2721px">Telefonnummer</div>
<div class="abs field" style="left:795px;top:2721px">E-mail</div>
<div class="abs field" style="left:614px;top:2769px;width:351px;height:84px">Ihre Nachricht</div>
<p class="abs consent">Durch Klicken auf die Schaltfläche stimmen Sie der Verarbeitung personenbezogener Daten zu</p>
<a class="abs btn submit">Absenden</a>
<div class="abs footer-rule"></div>
<footer>
  <span class="abs footer" style="left:235px">Lumivelde 2022</span>
  <span class="abs footer" style="left:857px">Impressum | &nbsp;Dotenschutz</span>
</footer>

</body>
</html>
```